Visitenkarte erstellen für Reiki Praxis

Visitenkarten für Reiki Praxis Doppelseitig

business cards reiki practice double-sided

The background can also be a different color

```html
<!DOCTYPE html>
<html lang="en">
<head>
<meta charset="utf-8">
<title>Quiet Current – Business Cards</title>
<link href="https://fonts.googleapis.com/css2?family=Raleway:wght@400;500;600&family=Ubuntu:wght@400;500&display=swap" rel="stylesheet">
<style>
  :root {
    --backdrop: #2a2a2c;
    --card-dark: #1e1d1f;
    --card-light: #f7f5f4;
    --ink: #4a4548;
    --plum: #8c3b68;
    --gold: #d9a21f;
    --white: #ffffff;
    --band-plum: #a0507e;
    --band-sage: #9aa08c;
    --band-peach: #f0a56a;
  }
  * { margin: 0; padding: 0; box-sizing: border-box; }
  html, body {
    width: 1200px; height: 874px; overflow: hidden;
    background: var(--backdrop);
  }
  .sheet { position: relative; width: 1200px; height: 874px; }
  .card {
    position: absolute; width: 640px; height: 366px;
    border-radius: 22px; overflow: hidden;
    box-shadow: 0 18px 40px rgba(0,0,0,.45);
  }
  /* back side */
  .card--back { left: 480px; top: 50px; background: var(--card-dark); }
  .back-pattern {
    position: absolute; inset: 0;
    background: linear-gradient(120deg, #3b3a3d 0%, #242326 45%, #1c1b1d 100%);
  }
  .back-mark {
    position: absolute; right: 70px; bottom: 48px;
    display: flex; align-items: center; gap: 8px;
    font-family: "Ubuntu", sans-serif; font-size: 15px; letter-spacing: 2px;
    color: var(--band-peach);
  }
  .back-mark .dot { width: 10px; height: 10px; border-radius: 50%; background: var(--band-peach); }
  /* front side */
  .card--front { left: 80px; top: 460px; background: var(--card-dark); }
  .front-art { position: absolute; inset: 0; }
  .brand {
    position: absolute; left: 70px; top: 70px; width: 300px; text-align: center;
  }
  .brand__name {
    font-family: "Ubuntu", sans-serif; font-weight: 400; font-size: 27px;
    letter-spacing: 1.5px; color: var(--white);
  }
  .brand__person {
    margin-top: 4px;
    font-family: "Ubuntu", sans-serif; font-size: 17px; letter-spacing: 7px;
    color: var(--gold);
  }
  .contact {
    position: absolute; right: 34px; top: 196px; text-align: right;
    font-family: "Raleway", sans-serif; color: var(--ink);
  }
  .contact__name { font-size: 22px; font-weight: 600; color: var(--plum); letter-spacing: .5px; }
  .contact__role { font-size: 14px; font-weight: 500; color: var(--gold); margin-bottom: 8px; }
  .contact__line {
    display: flex; justify-content: flex-end; align-items: center; gap: 9px;
    font-size: 13px; line-height: 19px;
  }
  .contact__line svg { width: 11px; height: 11px; flex: none; fill: var(--gold); }
  .contact__line .gap { width: 11px; flex: none; }
</style>
</head>
<body>
<main class="sheet">

  <section class="card card--back" aria-label="Card back">
    <div class="back-pattern" role="img" aria-label="Repeating silver foil lotus pattern across the card back"></div>
    <div class="back-mark"><span class="dot"></span>QUIET CURRENT</div>
  </section>

  <section class="card card--front" aria-label="Card front">
    <svg class="front-art" viewBox="0 0 640 366" width="640" height="366">
      <defs>
        <linearGradient id="bandGradient" x1="0" x2="1" y1="0" y2="0">
          <stop offset="0" stop-color="var(--band-peach)"/>
          <stop offset=".25" stop-color="var(--band-plum)"/>
          <stop offset=".6" stop-color="var(--band-sage)"/>
          <stop offset=".8" stop-color="var(--band-plum)"/>
          <stop offset="1" stop-color="var(--band-peach)"/>
        </linearGradient>
        <radialGradient id="softGlow" cx=".5" cy=".5" r=".5">
          <stop offset="0" stop-color="#eadfe2" stop-opacity=".7"/>
          <stop offset="1" stop-color="#eadfe2" stop-opacity="0"/>
        </radialGradient>
      </defs>
      <path d="M0,200 C120,292 260,292 380,222 C470,172 560,140 640,166 L640,178 C560,152 470,186 380,236 C260,304 120,304 0,214 Z" fill="url(#bandGradient)"/>
      <path d="M0,214 C120,304 260,304 380,236 C470,186 560,152 640,178 L640,366 L0,366 Z" fill="var(--card-light)"/>
      <ellipse cx="470" cy="280" rx="180" ry="110" fill="url(#softGlow)" role="img" aria-label="Faint large lotus line drawing behind the contact details"/>
    </svg>

    <div class="brand">
      <div class="brand__name">QUIET CURRENT</div>
      <div class="brand__person">MARA LENZ</div>
    </div>

    <div class="contact">
      <div class="contact__name">DANIEL REYES</div>
      <div class="contact__role">President</div>
      <div class="contact__line">555-014-2210
        <svg viewBox="0 0 24 24"><path d="M6.6 10.8a15 15 0 0 0 6.6 6.6l2.2-2.2a1 1 0 0 1 1-.25 11.4 11.4 0 0 0 3.6.6 1 1 0 0 1 1 1V20a1 1 0 0 1-1 1A17 17 0 0 1 3 4a1 1 0 0 1 1-1h3.5a1 1 0 0 1 1 1c0 1.25.2 2.45.6 3.6a1 1 0 0 1-.25 1z"/></svg></div>
      <div class="contact__line">hello@QuietCurrent.com
        <svg viewBox="0 0 24 24"><path d="M2 5h20v14H2z M2 5l10 8 10-8" fill="var(--gold)"/><path d="M3 6l9 7 9-7" fill="none" stroke="#fff" stroke-width="1.5"/></svg></div>
      <div class="contact__line">QuietCurrent.com
        <svg viewBox="0 0 24 24"><circle cx="12" cy="12" r="10"/><path d="M2 12h20M12 2c3 3 3 17 0 20M12 2c-3 3-3 17 0 20" fill="none" stroke="#fff" stroke-width="1.4"/></svg></div>
      <div class="contact__line">1420 Willow Bend Road
        <svg viewBox="0 0 24 24"><path d="M12 2a7 7 0 0 0-7 7c0 5 7 13 7 13s7-8 7-13a7 7 0 0 0-7-7zm0 9.5A2.5 2.5 0 1 1 12 6.5a2.5 2.5 0 0 1 0 5z"/></svg></div>
      <div class="contact__line">Fairview, Oregon 97024<span class="gap"></span></div>
    </div>
  </section>

</main>
</body>
</html>
```